Church Website with Home Page and Member Sermon Library

I am in need of an updated design for our church website. This will include 4 pages (outlined below). We are a conservative, evangelical, Christian church. The site should be modern and clean, while still reflecting our conservative values. I already have a logo for our church, and I want the site to incorporate the logo, and match the logo/branding. Stock photos are allowed if needed, but I have uploaded some images of our church and would prefer those images to be used if possible. Any stock photos used should not include any people in the photos (scenery, nature, buildings, animals, etc. are fine).

The site will need 4 pages: Home, Support Us (Donate), Login, and Recording Library.

Page 1: Home
The home page should include the following sections:

- Navigation: Should include links to each section of the home page plus a "listen live" link which will take the user to a live-streaming site and a "support us" link which will take the user to a support/donate page.

- Announcements: Can be either a banner or some other design, but there needs to be some way for us to post announcements for visitors to see. I'm open for creative ideas in this section, but would like it not to take up a lot of room on the page.

- About Us: Should include address, service times (see attached document), and information about the church.

- Pastor Bio: A section that introduces our pastor and gives a short bio about our pastor. Would like this section to include a picture of our pastor. Somewhere in this section I would like to include this Bible reference: "And I will give you pastors according to mine heart, which shall feed you with knowledge and understanding. Jer 3:15 KJV"

- Articles of Faith (What We Believe): This should include several sub-sections each with a heading, body, and possibly 1 or more scripture references. I have attached a document to the brief that includes our articles of faith. Feel free to be creative with this section in how you lay these out and format them.

- Support Us: A small section that explains what kind of support someone can give and a link to a donation page. The link can say something like "Support Us" or "Donate Now".

- Contact form: A contact form that allows the visitor to send us a message. The contact form should ask for name, email, phone, and message.

- Footer: A footer that will be displayed on all pages of the site. This should include at a minimum a link to the home page (or a link to each individual section in the home page if you prefer), a link to "listen live", a link to "support us", a link to "contact us" (or you can put the contact form directly in the footer if you prefer), the address, and a "member login" link.

Page 2: Support Us
The donation page should include a form the visitor can fill out to make a donation. We will embed a third party form later. For this design, please just mock out the design with a basic form asking for name, phone, and email.

Page 3: Login
The recording library (detailed below) will require members to login with a shared numeric code before accessing the page. We need a design for a login screen. The screen should include navigation/footer just like all other pages, but the body of the login page will consist only of a form that asks the user to enter the access code and then a "login" button.

Page 4: Recording Library

The library page is a member-only page that will require a shared, numeric pass code to access. On this page, members will be able to access a filterable list of past sermons. The page by default should display most recent sermons, but should also include a search form that allows the member to filter the sermon list to find a particular sermon. The search form should allow the user to select a filter type (e.g. Speaker name, date, event, etc.) and type in a value to search. They should be able to add multiple filters and remove filters that have been added. Each sermon that is displayed in the result list should include basic information such as title, date, speaker, tags, etc. along with a download icon, and an embedded audio player where they can click a play button to stream it on-demand. Each sermon should also have clickable tags associated with it that can be used to find related sermons.
Updates

Need extra days to review

I have uploaded several images of our church. Feel free to incorporate these into your design if possible.

Target Market(s)

Church Members

Industry/Entity Type

Religion

Number of Pages Required

4 page

Font styles to use
Sans Serif

Colors

Designer to choose colors to be used in the design.

Requirements
Must have
• Must incorporate the logo (attached)
Nice to have
• Would like the design to incorporate pictures of our church (attached) instead of stock photos if possible.
Should not have
• Please avoid an overly cluttered design. Stock photos used should not include any people in the photos.

```html
<!DOCTYPE html>
<html lang="en">
<head>
<meta charset="utf-8">
<title>Grace Covenant Church</title>
<link rel="stylesheet" href="https://fonts.googleapis.com/css2?family=Cinzel:wght@400&family=Montserrat:ital,wght@0,400;0,500;0,600;0,700;1,500&display=swap">
<style>
:root{
  --green:#7ca565;
  --green-dark:#6a9455;
  --cyan:#00b2d8;
  --text:#3f3f3f;
  --muted:#555;
  --line:#c9c9c9;
  --soft:#eef2f1;
  --white:#fff;
}
*{box-sizing:border-box;margin:0;padding:0}
html,body{width:1200px;height:4615px;overflow:hidden}
body{position:relative;background:var(--white);font-family:"Montserrat",sans-serif;color:var(--text)}
.abs{position:absolute}
.serif{font-family:"Cinzel",serif;font-weight:400;color:var(--green)}
.btn{position:absolute;display:flex;align-items:center;justify-content:center;border-radius:40px;color:#fff;font-weight:600;text-transform:uppercase;letter-spacing:.3px;text-decoration:none}
.btn-green{background:var(--green)}
.btn-cyan{background:var(--cyan)}

/* header */
.site-header{position:absolute;left:0;top:0;width:1200px;height:86px;background:#fff}
.brand{position:absolute;display:flex;align-items:center;gap:12px}
.brand-mark{width:18px;height:18px;background:var(--cyan)}
.brand-name{font-family:"Cinzel",serif;font-weight:400;color:var(--green);line-height:1.05;letter-spacing:2px}
.main-nav{position:absolute;left:358px;top:34px;display:flex;align-items:center;font-size:13px;color:#555}
.main-nav a{color:#555;text-decoration:none;text-transform:uppercase}
.main-nav .sep{display:inline-block;width:1px;height:16px;background:#aaa;margin:0 22px}

/* hero */
.hero-photo{position:absolute;left:0;top:86px;width:1200px;height:657px;background:linear-gradient(180deg,#e3e3e1 0%,#d9d8d4 30%,#a8826b 55%,#9a7660 72%,#b9b5ad 88%,#cfcdc8 100%)}
.welcome-box{position:absolute;left:356px;top:229px;width:484px;height:169px;background:rgba(255,255,255,.88);border:1.5px solid var(--green)}
.welcome-tag{position:absolute;left:507px;top:211px;width:197px;height:34px;background:var(--green);color:#fff;font-size:22px;letter-spacing:3px;display:flex;align-items:center;justify-content:center}
.hero-title{position:absolute;left:356px;top:262px;width:484px;text-align:center;font-size:44px;line-height:49px;letter-spacing:1px}
.announce-outline{position:absolute;left:131px;top:700px;width:940px;height:165px;border:3px solid #d8d8d8;border-top:none;border-radius:0 0 50px 0}
.announce{position:absolute;left:140px;top:663px;width:926px;height:193px;background:var(--green);border-radius:44px 0 44px 0;color:#fff;text-align:center}
.announce h2{font-family:"Cinzel",serif;font-weight:400;font-size:33px;letter-spacing:1px;margin-top:42px}
.announce .lead{font-weight:700;font-size:15px;margin-top:10px}
.announce .sub{font-size:15px;margin-top:8px}

/* about */
.about-frame{position:absolute;left:430px;top:942px;width:675px;height:482px;border:2px solid var(--cyan)}
.photo{position:absolute}
.bar-v,.bar-h{position:absolute}
.about-copy{position:absolute;left:595px;top:995px;width:460px}
.section-title{font-family:"Cinzel",serif;font-weight:400;color:var(--green);font-size:37px;letter-spacing:.5px}
.body-copy{font-size:14.5px;line-height:28px;color:var(--muted)}
.timing-label{color:var(--green);font-weight:700;font-size:16px;margin-top:24px;margin-left:3px}
.timing{display:grid;grid-template-columns:242px 250px;row-gap:14px;margin-top:16px;margin-left:3px;font-size:12.5px;font-weight:600;color:#222}

/* pastor */
.pastor-bg{position:absolute;left:0;top:1504px;width:1200px;height:609px;background:linear-gradient(180deg,#eef2f3 0%,#e9eeee 60%,#e2e9e8 100%)}
.underline{position:absolute;height:3px;background:var(--green)}
.quote{position:absolute;left:152px;top:1863px;width:473px;height:105px;background:var(--cyan);border-radius:0 32px 32px 0;color:#fff;padding:24px 40px 0 43px;font-size:14px;line-height:21px}
.quote em{font-weight:500}
.quote strong{display:block;font-weight:600;margin-top:4px;font-size:14px}

/* articles */
.faith-title{position:absolute;left:0;top:2178px;width:1200px;text-align:center;font-size:40px}
.rail{position:absolute;width:1.5px;background:var(--line)}
.dot{position:absolute;width:12px;height:12px;border-radius:50%;background:var(--green)}
.article{position:absolute}
.article h3{font-size:21px;font-weight:500;letter-spacing:3px;color:#2f6b4d;text-transform:uppercase;line-height:26px}
.article p{font-size:13.5px;line-height:25.8px;color:var(--muted);margin-top:8px}
.article .small{font-size:12.5px;line-height:25.5px}
.article ol{list-style:none;font-size:12.5px;line-height:31px;color:var(--muted);margin-top:4px}

/* support */
.support-frame{position:absolute;left:390px;top:3161px;width:668px;height:428px;border:2px solid var(--green)}

/* contact */
.contact-bg{position:absolute;left:0;top:3677px;width:1200px;height:571px;background:linear-gradient(180deg,#f1f4f2 0%,#edf1ee 55%,#d9ddd6 75%,#c8bfb3 88%,#dfe3dd 100%)}
.tag{position:absolute;background:var(--green);color:#fff;display:flex;align-items:center;justify-content:center;letter-spacing:2px}
.field{position:absolute;background:#fff;border:1px solid #cfcfcf;font-size:13px;color:#555;padding:0 20px;display:flex;align-items:center}
.field.tall{align-items:flex-start;padding-top:14px}

/* footer */
.site-footer{position:absolute;left:0;top:4248px;width:1200px;height:307px;background:#fff}
.vline{position:absolute;top:4253px;width:1.5px;height:290px;background:#e2e2e2}
.vline::before{content:"";position:absolute;left:0;top:62px;width:1.5px;height:24px;background:var(--cyan)}
.foot-head{position:absolute;font-size:14.5px;letter-spacing:2.5px;color:#2f6b4d;text-transform:uppercase}
.foot-links{position:absolute;left:425px;top:4342px;list-style:none;font-size:13px;line-height:30px;color:#555}
.foot-text{position:absolute;font-size:12.5px;line-height:19px;color:#555}
.copyright{position:absolute;left:0;top:4555px;width:1200px;height:60px;background:#eeeeee;display:flex;align-items:center;justify-content:center;font-size:12px;color:#666}
</style>
</head>
<body>

<header class="site-header">
  <a class="brand" style="left:118px;top:18px">
    <span class="brand-mark"></span>
    <span class="brand-name" style="font-size:18px">GRACE COVENANT<br>CHURCH</span>
  </a>
  <nav class="main-nav">
    <a>About Us</a><span class="sep"></span>
    <a>Pastor Bio</a><span class="sep"></span>
    <a>Articles of Faith</a><span class="sep"></span>
    <a>Contact</a>
  </nav>
  <a class="btn btn-green" style="left:840px;top:25px;width:120px;height:36px;font-size:12px;font-weight:500">Listen Live</a>
  <a class="btn btn-cyan" style="left:967px;top:25px;width:120px;height:36px;font-size:12px;font-weight:500">Support Us</a>
</header>

<section class="hero">
  <div class="hero-photo" role="img" aria-label="Photograph of the brick church building with its sign under an overcast sky"></div>
  <div class="welcome-box"></div>
  <div class="welcome-tag serif" style="color:#fff">WELCOME TO</div>
  <h1 class="hero-title serif">GRACE COVENANT<br>CHURCH</h1>
  <a class="btn btn-cyan" style="left:514px;top:376px;width:172px;height:39px;font-size:13px">Listen Live</a>
  <div class="announce-outline"></div>
  <div class="announce">
    <h2>ANNOUNCEMENT</h2>
    <p class="lead">LOREM IPSUM DOLOR SIT AMET CONSECTETUR ADIPISCING</p>
    <p class="sub">Ut enim ad minim veniam quis nostrud exercitation Allamco laboris nisi ut aliquip ex ea</p>
  </div>
</section>

<section class="about">
  <div class="about-frame"></div>
  <div class="bar-v" style="left:118px;top:1101px;width:8px;height:286px;background:var(--cyan)"></div>
  <div class="bar-h" style="left:118px;top:1379px;width:235px;height:8px;background:var(--cyan)"></div>
  <div class="photo" style="left:136px;top:983px;width:419px;height:385px;background:linear-gradient(180deg,#cfd2d2 0%,#c8c9c7 35%,#9b7b66 55%,#8d705e 65%,#b8b8b6 78%,#c9c9c7 100%)" role="img" aria-label="Photograph of the church building and its parking lot"></div>
  <div class="about-copy">
    <h2 class="section-title">ABOUT OUR CHURCH</h2>
    <p class="body-copy" style="margin-top:20px">Lorem ipsum dolor sit amet, consectetur adipiscing elit, sed do eiusmod tempor incididunt ut labore et dolore magna aliqua. Ut enim ad minim veniam, quis nostrud exercitation</p>
    <p class="body-copy" style="margin-top:6px">Allamco laboris nisi ut aliquip ex ea commodo consequat. Duis aute irure dolor in reprehenderit in voluptate velit esse cillum dolore eu fugiat nulla pariatur.</p>
    <p class="timing-label">SERVICE TIMING:</p>
    <div class="timing">
      <span>Wednesday Night Service: 7:30 PM</span><span>Sunday Morning Service: 11:00 AM</span>
      <span>Sunday School: 10:00 AM</span><span>Sunday Night Service: 5:30 PM</span>
    </div>
  </div>
</section>

<section class="pastor">
  <div class="pastor-bg" role="img" aria-label="Faded photograph of the church grounds behind the section"></div>
  <h2 class="section-title abs" style="left:156px;top:1615px;font-size:42px">OUR PASTOR</h2>
  <div class="underline" style="left:159px;top:1674px;width:95px"></div>
  <p class="body-copy abs" style="left:159px;top:1704px;width:470px;font-size:13.5px;line-height:25px">Lorem ipsum dolor sit amet, consectetur adipiscing elit, sed do eiusmod tempor incididunt ut labore et dolore magna aliqua. Ut enim ad minim veniam quis nostrud exercitation Allamco laboris nisi ut aliquip ex ea commodo consequat. Duis aute irure dolor in reprehenderit in voluptate velit.Lorem ipsum dolor sit amet, consectetur adipiscing elit,</p>
  <div class="quote"><em>“And I will give you pastors according to mine heart, which shall feed you with knowledge and understanding”</em><strong>Jer 3:15 KJV</strong></div>
  <div class="abs" style="left:679px;top:1607px;width:354px;height:370px;border:1.5px solid #9aa39a"></div>
  <div class="abs" style="left:931px;top:1875px;width:122px;height:117px;background:var(--green)"></div>
  <div class="photo" style="left:693px;top:1619px;width:346px;height:360px;background:linear-gradient(160deg,#eceff0 0%,#dfe3e4 45%,#3a3a3c 70%,#1f1f21 100%)" role="img" aria-label="Portrait of the pastor holding a Bible"></div>
</section>

<section class="faith">
  <h2 class="faith-title serif">ARTICLES OF FAITH</h2>
  <div class="underline" style="left:555px;top:2233px;width:90px"></div>
  <div class="rail" style="left:146px;top:2312px;height:600px"></div>
  <div class="rail" style="left:649px;top:2312px;height:603px"></div>

  <span class="dot" style="left:141px;top:2306px"></span>
  <div class="article" style="left:177px;top:2305px;width:430px">
    <h3>The God Head.</h3>
    <p>We believe in the God head bodily, known as the Divine Trinity. This body consist of God the father, Jesus Christ, his only begotten son and the redeemer of the world, and of the Holy Ghost, The third person of the Divine Trinity.</p>
  </div>

  <span class="dot" style="left:141px;top:2536px"></span>
  <div class="article" style="left:177px;top:2525px;width:430px">
    <h3>Full Salvation</h3>
    <p class="small">We believe that Salvation is received only when a person comes to the realization that he or she is lost and separated from God and becomes full of godly sorrow, confessing their sins and true repentance, believing in the shed blood of the Lord Jesus Christ as the only sacrifice for sins. Through the blood of Christ we have:</p>
    <ol>
      <li>(1) remission of sins, Matthew 26:28 Heb 9:22</li>
      <li>(2) Sanctification. Hebrews 13:12</li>
      <li>(3) redemption. Revelations 5:9</li>
      <li>(4) cleansing. 1 John 1:7 Rev. 1:5</li>
      <li>(5). Justification. Romans 5:9</li>
    </ol>
  </div>

  <span class="dot" style="left:141px;top:2902px"></span>
  <div class="article" style="left:179px;top:2892px;width:420px">
    <h3>Sanctification</h3>
    <p>“Sanctify them through thy truth thy word is truth St John 17:17. For this is the will of God even your sanctification”</p>
    <p style="margin-top:6px">We believe in a set apart life, separate from the world to Christ 2 Cor 6:17-18</p>
  </div>

  <span class="dot" style="left:644px;top:2306px"></span>
  <div class="article" style="left:679px;top:2305px;width:445px">
    <h3>Baptism of the Holy Ghost</h3>
    <p>We believe in the baptism of the Holy Ghost as it is taught in the Bible and promised by our Lord Jesus Christ, with speaking in tongues as the Spirit gives utterance as the initial evidence. Acts 2:4 we believe that the gift of the Holy Ghost is for all believers as the Lord promised. Acts 2:17-1</p>
  </div>

  <span class="dot" style="left:644px;top:2538px"></span>
  <div class="article" style="left:679px;top:2527px;width:440px">
    <h3>Divine Healing</h3>
    <p>We believe Divine Healing to be included in the atonement of Jesus Christ our Lord, And believe that it is still for us today. 1 Peter 2:24 Luke 9:1-2 Mark 16-18 James 5:15</p>
  </div>

  <span class="dot" style="left:644px;top:2726px"></span>
  <div class="article" style="left:679px;top:2717px;width:430px">
    <h3>Second Coming of Christ</h3>
    <p>We believe in the second coming of Jesus Christ. Matthew 24:44 Luke 12:40</p>
  </div>

  <span class="dot" style="left:644px;top:2910px"></span>
  <div class="article" style="left:679px;top:2899px;width:430px">
    <h3>Eternity</h3>
    <p>We believe in Literal Eternity. Eternal Life for the believer and eternal death for those without Christ. Revelations 21:1-27</p>
  </div>
</section>

<section class="support">
  <div class="support-frame"></div>
  <div class="bar-v" style="left:154px;top:3310px;width:7px;height:236px;background:var(--cyan)"></div>
  <div class="bar-h" style="left:154px;top:3539px;width:199px;height:7px;background:var(--cyan)"></div>
  <div class="photo" style="left:167px;top:3209px;width:388px;height:328px;background:linear-gradient(135deg,#8fb35a 0%,#a9c77a 40%,#dfe6d2 70%,#f2f2f0 100%)" role="img" aria-label="Photograph of a coin jar labelled for donations"></div>
  <h2 class="section-title abs" style="left:609px;top:3242px">SUPPORT US</h2>
  <p class="abs" style="left:609px;top:3318px;width:410px;font-size:16.5px;line-height:29px;color:#444">Lorem ipsum dolor sit amet, consectetur adipiscing elit, sed do eiusmod tempor incididunt ut labore et dolore magna aliqua. Ut enim ad minim veniam, quis nostrud exercitation</p>
  <a class="btn btn-green" style="left:607px;top:3457px;width:185px;height:41px;font-size:13px">Donate Now</a>
</section>

<section class="contact">
  <div class="contact-bg" role="img" aria-label="Faded photograph of a brick church with a white steeple among trees"></div>
  <div class="tag" style="left:518px;top:3729px;width:163px;height:29px;font-size:15px;font-family:'Cinzel',serif">GET IN TOUCH</div>
  <h2 class="section-title abs" style="left:0;top:3765px;width:1200px;text-align:center;font-size:42px">CONTACT US</h2>
  <div class="underline" style="left:561px;top:3819px;width:88px"></div>
  <div class="field" style="left:204px;top:3860px;width:391px;height:53px">First Name</div>
  <div class="field" style="left:604px;top:3860px;width:392px;height:53px">Last Name</div>
  <div class="field" style="left:204px;top:3926px;width:391px;height:52px">Email address</div>
  <div class="field" style="left:604px;top:3926px;width:392px;height:52px">Phone</div>
  <div class="field tall" style="left:204px;top:3990px;width:792px;height:99px">Message</div>
  <a class="btn btn-cyan" style="left:503px;top:4112px;width:196px;height:45px;font-size:14px;font-weight:500">Send Message</a>
</section>

<footer class="site-footer">
  <a class="brand" style="left:134px;top:54px">
    <span class="brand-mark"></span>
    <span class="brand-name" style="font-size:21px">GRACE COVENANT<br>CHURCH</span>
  </a>
</footer>
<div class="vline" style="left:396px"></div>
<div class="vline" style="left:596px"></div>
<div class="vline" style="left:851px"></div>
<h4 class="foot-head" style="left:423px;top:4305px;font-weight:400">Navigation</h4>
<ul class="foot-links">
  <li>About Us</li><li>Paster Bio</li><li>Article of Faith</li><li>Listen Live</li><li>Contact Us</li>
</ul>
<h4 class="foot-head" style="left:618px;top:4305px;font-weight:400">Donation</h4>
<p class="foot-text" style="left:620px;top:4341px;width:210px">Lorem ipsum dolor sit amet, consectetur adipiscing elit, sed do eiusmod tempor inci</p>
<a class="btn btn-green" style="left:616px;top:4422px;width:133px;height:29px;font-size:10.5px;font-weight:500">Donate Now</a>
<h4 class="foot-head" style="left:881px;top:4305px;font-weight:400">Contact Us</h4>
<svg class="abs" style="left:876px;top:4341px" width="36" height="36" viewBox="0 0 36 36" aria-hidden="true">
  <circle cx="18" cy="18" r="17" fill="#7ca565"/>
  <path d="M18 8a7 7 0 0 0-7 7c0 5.2 7 12.5 7 12.5s7-7.3 7-12.5a7 7 0 0 0-7-7z" fill="#fff"/>
  <circle cx="18" cy="15" r="2.6" fill="#7ca565"/>
</svg>
<p class="foot-text" style="left:922px;top:4341px;width:170px;font-size:12px;line-height:17px;color:#333">28 Cedar Lane, Suite 210, Millbrook, NY 12545 USA</p>
<a class="btn btn-cyan" style="left:876px;top:4415px;width:132px;height:29px;font-size:10.5px;font-weight:500">Member Login</a>
<div class="copyright">© 2023 Grace Covenant Church. All Rights Reserved</div>

</body>
</html>
```